Roofing Company Modern look

I want a modern and sophisticated look for our roofing business.

Our address is :

4276 Pellman Crossing Rd
Orlando, Fl 32825

(407)-583-2716

www.SummitcrestShinglesFl.com

I also want to make sure on the back there is a spot to put
Project Manager Name :

Number:

Because the cards will be used by all sales people

Project Manager Name :

Also there are accreditation we have logos are uploaded here as well that I would like maybe on the back of card as well

I also want to highlight our special attributions or trades:

Residential & Commercial
Fully Insured
License # CCC4872196
Insurance Claims
Serving Central Florida Since 1992
Free Estimates

Contact Information for Business Card

Our address is :

4276 Pellman Crossing Rd
Orlando, Fl 32825

(407)-583-2716

Project Manager Name :

Residential & Commercial
Fully Insured
License # CCC4872196
Insurance Claims
Free Estimates

Font styles to use
Serif
Sans Serif

Colors
3176b5

Requirements
Must have
• Must have royal blue like my logo grey and black are the colors I like

```html
<!DOCTYPE html>
<html lang="en">
<head>
<meta charset="UTF-8">
<title>Summitcrest Shingles &amp; Gutters – Business Card</title>
<link href="https://fonts.googleapis.com/css2?family=Arimo:wght@400;700&display=swap" rel="stylesheet">
<style>
  :root {
    --backdrop: #b4b4b4;
    --card: #ffffff;
    --ink: #222222;
    --ink-soft: #333333;
    --label-grey: #a9a9a9;
    --rule-grey: #8a8a8a;
    --royal-blue: #3176b5;
    --badge-fill: #e3e8ee;
    --badge-edge: #9aa6b2;
  }
  * { margin: 0; padding: 0; box-sizing: border-box; }
  html, body {
    width: 1200px; height: 1200px; overflow: hidden;
    background: var(--backdrop);
    font-family: "Arimo", Arial, sans-serif;
  }
  .canvas { position: relative; width: 1200px; height: 1200px; }

  .card {
    position: absolute; top: 303px; height: 594px;
    background: var(--card);
  }
  .card--back { left: 200px; width: 370px; }
  .card--front { left: 599px; width: 364px; }

  /* Back side */
  .name-field { position: absolute; left: 45px; top: 124px; width: 279px; }
  .name-field__label {
    font-size: 17px; font-weight: 700; letter-spacing: 0.5px;
    color: var(--label-grey);
  }
  .name-field__rule {
    margin-top: 11px; height: 1px; background: var(--rule-grey);
  }

  .services {
    position: absolute; left: 0; right: 0; top: 219px;
    list-style: none; text-align: center;
  }
  .services li {
    font-size: 15px; line-height: 29px; color: var(--ink);
    letter-spacing: 0.2px;
  }

  .badges { position: absolute; left: 0; top: 0; width: 370px; height: 594px; }
  .badge { fill: var(--badge-fill); stroke: var(--badge-edge); stroke-width: 1; }

  /* Front side */
  .brand {
    position: absolute; left: 0; right: 0; top: 188px; text-align: center;
    color: var(--royal-blue); font-weight: 400;
  }
  .brand__name { font-size: 34px; letter-spacing: 3px; line-height: 1; }
  .brand__sub {
    margin-top: 8px; font-size: 11.5px; letter-spacing: 2.6px;
    text-transform: uppercase;
  }

  .contact {
    position: absolute; left: 0; right: 0; top: 422px; text-align: center;
    color: var(--ink-soft); font-size: 19px; line-height: 24px;
  }
  .contact__rule {
    width: 101px; height: 1px; background: #bdbdbd; margin: 12px auto 13px;
  }
</style>
</head>
<body>
<div class="canvas">

  <section class="card card--back">
    <div class="name-field">
      <div class="name-field__label">NAME:</div>
      <div class="name-field__rule"></div>
    </div>

    <ul class="services">
      <li>RESIDENTIAL &amp; COMMERCIAL</li>
      <li>LICENSE # CCC4872196</li>
      <li>SERVING CENTRAL FLORIDA SINCE 1992</li>
      <li>FREE ESTIMATES</li>
      <li>FULLY INSURED</li>
      <li>INSURANCE CLAIMS</li>
    </ul>

    <svg class="badges" viewBox="0 0 370 594" role="img" aria-label="Accreditation badges of partner programs and listings">
      <rect class="badge" x="119.5" y="427.5" width="132" height="37" rx="3"/>
      <rect class="badge" x="50.5" y="491.5" width="92" height="81" rx="6"/>
      <rect class="badge" x="171.5" y="492.5" width="80" height="73" rx="6"/>
      <rect class="badge" x="272.5" y="479.5" width="53" height="84" rx="6"/>
    </svg>
  </section>

  <section class="card card--front">
    <div class="brand">
      <div class="brand__name">SUMMITCREST</div>
      <div class="brand__sub">Shingles &amp; Gutters Inc.</div>
    </div>

    <div class="contact">
      <p>4276 Pellman Crossing Rd</p>
      <p>Orlando, Fl 32825</p>
      <div class="contact__rule"></div>
      <p>(407)-583-2716</p>
      <p>www.SummitcrestShinglesFl.com</p>
    </div>
  </section>

</div>
</body>
</html>
```